Personal Training Business Card Design

I have just started my own personal training business called "Lana Corvell Fitness". My goal as a personal trainer is to motivate, inspire and educate all of my clients about the benefits of regular exercise, nourishing the body with nutritious foods and living healthy. I train both men and women, so I would like a business card that will appeal to both sexes and not come across too feminine or too masculine. I'm looking for a fresh, yet simple look which uses "fresh" colours such as green, white and grey - similar to my logo (but open to other effective gender-neutral colour schemes). I am open to using the logo I have uploaded as one image together, or separating the text and image (also supplied).
Industry/Entity Type
Personal Trainer
Contact Information for Business Card
Lana Corvell
Fitness Coach
Address: Ground Floor, Maplewick House, 342 Larkin St, Brisbane City, 4000
Email: lanacorvellfitness@mailorbit.net
Phone: 0455 293 604
Socialnook: www.socialnook.net/lanacorvellfitness
Look and feel

```html
<!DOCTYPE html>
<html lang="en">
<head>
<meta charset="utf-8">
<title>Lana Corvell Fitness – Business Card</title>
<link rel="stylesheet" href="https://fonts.googleapis.com/css2?family=Josefin+Sans:wght@300&family=Dosis:wght@500;600&display=swap">
<style>
  :root {
    --green: #8bc542;
    --green-icon: #7cc04a;
    --leaf-light: #dbe99c;
    --leaf-mid: #b9d66e;
    --grey-text: #7b7b7b;
    --white: #ffffff;
  }
  * { margin: 0; padding: 0; box-sizing: border-box; }
  html, body { width: 1200px; height: 736px; overflow: hidden; background: var(--white); }
  .card { position: relative; width: 1200px; height: 736px; background: var(--white); overflow: hidden; }
  .card__band { position: absolute; inset: 0; }
  .card__name {
    position: absolute; left: 66px; top: 74px;
    font-family: "Josefin Sans", sans-serif; font-weight: 300;
    font-size: 94px; line-height: 1; letter-spacing: 3px;
    color: var(--white); white-space: nowrap;
  }
  .brand {
    position: absolute; left: 894px; top: 29px; width: 256px; height: 256px;
    border: 3px solid var(--white); border-radius: 50%;
    display: flex; align-items: center; justify-content: center; text-align: center;
  }
  .brand__name {
    font-family: "Dosis", sans-serif; font-weight: 600;
    font-size: 36px; line-height: 1.1; color: var(--white); letter-spacing: 1px;
  }
  .artwork {
    position: absolute; left: 1020px; top: 424px; width: 180px; height: 290px;
    border-radius: 28px 0 0 28px;
    background: linear-gradient(160deg, var(--leaf-light), var(--leaf-mid));
  }
  .contact { position: absolute; left: 76px; top: 0; list-style: none; }
  .contact__item { position: absolute; left: 0; display: flex; align-items: flex-start; }
  .contact__icon { width: 52px; height: 52px; flex: none; }
  .contact__text {
    position: absolute; left: 85px; white-space: nowrap;
    font-family: "Dosis", sans-serif; font-weight: 500;
    font-size: 29px; line-height: 38px; color: var(--grey-text);
  }
  .contact__item--address { top: 361px; }
  .contact__item--address .contact__text { top: -30px; }
  .contact__item--email { top: 466px; }
  .contact__item--email .contact__text { top: 6px; }
  .contact__item--phone { top: 539px; }
  .contact__item--phone .contact__text { top: 6px; }
  .contact__item--social { top: 614px; }
  .contact__item--social .contact__text { top: 6px; }
</style>
</head>
<body>
<main class="card">
  <svg class="card__band" width="1200" height="736" viewBox="0 0 1200 736" aria-hidden="true">
    <path d="M0 0 H1200 V540 C1040 370 820 255 560 232 C330 214 150 222 0 238 Z" fill="var(--green)"/>
  </svg>

  <h1 class="card__name">LANA CORVELL</h1>

  <div class="brand">
    <span class="brand__name">Lana Corvell<br>Fitness</span>
  </div>

  <div class="artwork" role="img" aria-label="Illustration of two green leaves with a brown stem"></div>

  <ul class="contact">
    <li class="contact__item contact__item--address">
      <svg class="contact__icon" viewBox="0 0 52 52" aria-hidden="true">
        <path d="M4 26 L26 6 L48 26 H41 V48 H11 V26 Z" fill="var(--green-icon)"/>
        <rect x="21" y="32" width="10" height="16" fill="var(--white)"/>
      </svg>
      <p class="contact__text">Ground Floor, Maplewick House<br>342 Larkin St,<br>Brisbane City, 4000</p>
    </li>
    <li class="contact__item contact__item--email">
      <svg class="contact__icon" viewBox="0 0 52 52" aria-hidden="true">
        <rect x="2" y="4" width="46" height="32" rx="2" fill="var(--green-icon)"/>
        <rect x="18" y="36" width="14" height="6" fill="var(--green-icon)"/>
        <rect x="12" y="42" width="26" height="4" fill="var(--green-icon)"/>
      </svg>
      <p class="contact__text">lanacorvellfitness@mailorbit.net</p>
    </li>
    <li class="contact__item contact__item--phone">
      <svg class="contact__icon" viewBox="0 0 52 52" aria-hidden="true">
        <path d="M12 4 C6 6 3 12 6 22 C11 36 22 46 34 49 C40 50 44 47 45 43 L38 35 C35 34 33 37 31 39 C25 36 17 28 14 21 C17 19 20 17 19 14 Z" fill="var(--green-icon)"/>
      </svg>
      <p class="contact__text">0455 293 604</p>
    </li>
    <li class="contact__item contact__item--social">
      <svg class="contact__icon" viewBox="0 0 52 52" aria-hidden="true">
        <g fill="none" stroke="var(--green-icon)" stroke-width="3.5">
          <circle cx="23" cy="23" r="19"/>
          <ellipse cx="23" cy="23" rx="8" ry="19"/>
          <line x1="4" y1="23" x2="42" y2="23"/>
          <path d="M8 13 H38 M8 33 H38"/>
        </g>
      </svg>
      <p class="contact__text">www.socialnook.net/lanacorvellfitness</p>
    </li>
  </ul>
</main>
</body>
</html>
```